Kelvane Plumbing Business cards

Company is Kelvane Plumbing.
name Dashel Morrowby, I am a plumber, drainer, gasfitter and roofer
Mobile: 0431 906 154
Email address: info@kelvaneplumbing.example (check out my website for some ideas)
Website: www.kelvaneplumbing.example
ABN: 82 916 203 471
LIC: 604517K

I am reliable all round plumber. I am a 24 hour emergency service. Kelvane Plumbing is a professional plumbing service in the Illawarra, South Coast, Southern Sydney and Southern Highland regions of NSW. We offer a 24 hour emergency service for piece of mind to our customers. Call us now to see how we can help you. Kelvane Plumbing approaches every job with attention to detail and excellent customer service. With our superior workmanship you can be confident that the job will be done right the first time around. You can rest assured with results that are guaranteed to last.

Target Market(s)

the general public

Contact Information for Business Card

look up website for some ideas something with similar colours to logo and new modern and to catch the eye.

Colors
fdfdfd
ffffff
000000
7f7f7f
aaaaaa
33a6d7
0492cd

Requirements
Must have
• all contact details
• company- Kelvane Plumbing
• name- Dashel Morrowby
• number mobile- 0431 906 154
• Email address- info@kelvaneplumbing.example
• Website- www.kelvaneplumbing.example
• ABN- 82 916 203 471
• LIC- 604517K

```html
<!DOCTYPE html>
<html lang="en">
<head>
<meta charset="utf-8">
<title>Kelvane Plumbing – Business Cards</title>
<link href="https://fonts.googleapis.com/css2?family=Montserrat:wght@600&family=PT+Sans:wght@400;700&display=swap" rel="stylesheet">
<style>
  :root {
    --backdrop: #3d3d3d;
    --card-dark: #141414;
    --card-light: #e6e6e6;
    --brand-blue: #33a6d7;
    --brand-blue-deep: #0492cd;
    --ink: #000000;
    --white: #ffffff;
  }
  * { margin: 0; padding: 0; box-sizing: border-box; }
  html, body {
    width: 1200px; height: 1200px; overflow: hidden;
    background: var(--backdrop);
  }
  .card {
    position: absolute;
    left: 290px;
    width: 630px;
    height: 358px;
    background: var(--card-dark);
    overflow: hidden;
  }
  .card--front { top: 176px; }
  .card--back { top: 642px; }

  .brand-name {
    font-family: "Montserrat", sans-serif;
    font-weight: 600;
    color: var(--brand-blue);
    text-align: center;
    position: absolute;
    left: 0; right: 0;
    white-space: nowrap;
  }
  .card--front .brand-name { top: 158px; font-size: 34px; }
  .card--back .brand-name { top: 78px; font-size: 38px; }

  .wave { position: absolute; left: 0; top: 0; width: 630px; height: 358px; }

  .holder {
    position: absolute;
    right: 384px;
    top: 246px;
    text-align: right;
    font-family: "PT Sans", sans-serif;
    color: var(--ink);
    white-space: nowrap;
  }
  .holder__name { font-weight: 700; font-size: 24px; line-height: 30px; }
  .holder__meta { font-size: 19px; line-height: 22px; margin-top: 2px; }

  .divider {
    position: absolute;
    left: 262px; top: 254px;
    width: 3px; height: 84px;
    background: var(--ink);
  }
  .contacts {
    position: absolute;
    left: 284px; top: 252px;
    list-style: none;
    font-family: "PT Sans", sans-serif;
    font-size: 19px;
    color: var(--ink);
    white-space: nowrap;
  }
  .contacts li { display: flex; align-items: center; height: 29px; }
  .contacts svg { width: 20px; height: 20px; margin-right: 12px; flex: none; }
</style>
</head>
<body>
  <section class="card card--front">
    <div class="brand-name">Kelvane Plumbing</div>
  </section>

  <section class="card card--back">
    <div class="brand-name">Kelvane Plumbing</div>

    <svg class="wave" viewBox="0 0 630 358" aria-hidden="true">
      <path d="M0,186 C110,228 210,240 310,228 C420,214 520,176 630,198 V358 H0 Z" fill="var(--card-light)"/>
      <path d="M140,237 C290,232 410,150 630,168 L630,190 C520,170 420,212 310,228 C240,236 190,238 140,237 Z" fill="var(--brand-blue)"/>
      <path d="M0,156 C70,190 170,222 265,229" fill="none" stroke="var(--card-light)" stroke-width="3"/>
    </svg>

    <div class="holder">
      <div class="holder__name">Dashel Morrowby</div>
      <div class="holder__meta">ABN- 82 916 203 471</div>
      <div class="holder__meta">LIC- 604517K</div>
    </div>

    <div class="divider"></div>

    <ul class="contacts">
      <li>
        <svg viewBox="0 0 24 24" aria-hidden="true"><circle cx="12" cy="12" r="12" fill="#000"/><path d="M8.2 6.5l2 2.3-1.1 1.6c.8 1.7 2 2.9 3.6 3.7l1.6-1.1 2.3 2-1.2 2c-4.6-.4-8.6-4.4-9-9z" fill="#fff"/></svg>
        0431 906 154
      </li>
      <li>
        <svg viewBox="0 0 24 24" aria-hidden="true"><circle cx="12" cy="12" r="12" fill="#000"/><rect x="6" y="8" width="12" height="8.5" rx="1" fill="#fff"/><path d="M6.5 8.5l5.5 4 5.5-4" fill="none" stroke="#000" stroke-width="1.3"/></svg>
        info@kelvaneplumbing.example
      </li>
      <li>
        <svg viewBox="0 0 24 24" aria-hidden="true"><circle cx="12" cy="12" r="12" fill="#000"/><circle cx="12" cy="12" r="6.5" fill="none" stroke="#fff" stroke-width="1.5"/><path d="M5.5 12h13M12 5.5c-2.6 3.6-2.6 9.4 0 13M12 5.5c2.6 3.6 2.6 9.4 0 13" fill="none" stroke="#fff" stroke-width="1.2"/></svg>
        www.kelvaneplumbing.example
      </li>
    </ul>
  </section>
</body>
</html>
```